Business Card & Stationary for Belmora Yards
1 sided business card and stationary
Modern
Trevor Hollis
WPMB Certified Applicator
48260 Pinecrest
Westbrook, KS 66019
trevor@belmorayards.com
belmorayards.com
I like business cards that use the symbols for phone, web, and email rather than using the words.
I would also like to list my services on the card. They could all be listed on one line at the bottom of the card with bullets between them or wherever they may fit best with the rest of the design.
"Fertilization"
"Weed Control"
"Aeration"
"Verticutting"
"Seeding"
Should be plain white with nothing printed on it. (1 sided business card please)
Logo to use on card

```html
<!DOCTYPE html>
<html lang="en">
<head>
<meta charset="utf-8">
<title>Belmora Yards – Business Card</title>
<link href="https://fonts.googleapis.com/css2?family=Open+Sans:ital,wght@0,400;0,600;0,700;1,600&display=swap" rel="stylesheet">
<style>
  :root {
    --backdrop: #3b3b3b;
    --card-white: #ffffff;
    --band-brown: #6e2410;
    --name-brown: #6a2612;
    --leaf-green: #5fa42a;
    --line-green: #6aaa2e;
    --text-grey: #4a4a4a;
    --divider-grey: #d9d9d9;
  }
  * { box-sizing: border-box; margin: 0; padding: 0; }
  html, body {
    width: 1200px; height: 780px; overflow: hidden;
    background: var(--backdrop);
    font-family: "Open Sans", Arial, sans-serif;
  }
  .card {
    position: absolute; left: 100px; top: 105px;
    width: 1000px; height: 570px;
    background: var(--card-white);
    border-radius: 44px;
    overflow: hidden;
  }
  .side-band {
    position: absolute; top: 0; bottom: 0; width: 56px;
    background: var(--band-brown);
  }
  .side-band.left { left: 0; }
  .side-band.right { right: 0; }
  .edge-rule {
    position: absolute; top: 0; bottom: 0; width: 3px;
    background: var(--line-green);
  }
  .edge-rule.left { left: 72px; }
  .edge-rule.right { right: 72px; }

  .brand {
    position: absolute; left: 100px; top: 190px;
    width: 400px; height: 120px;
    display: flex; align-items: center; justify-content: center; gap: 16px;
  }
  .brand-dot {
    width: 30px; height: 30px; border-radius: 50%;
    background: var(--leaf-green);
    flex: none;
  }
  .brand-name {
    font-size: 48px; font-weight: 700; color: var(--name-brown);
    white-space: nowrap;
  }

  .column-divider {
    position: absolute; left: 528px; top: 48px;
    width: 2px; height: 270px;
    background: linear-gradient(var(--divider-grey), rgba(217,217,217,0));
  }

  .contact {
    position: absolute; left: 548px; top: 40px;
    color: var(--text-grey);
  }
  .person-name {
    font-size: 42px; font-weight: 700; color: var(--name-brown); line-height: 1.1;
  }
  .person-title {
    font-size: 23px; font-weight: 600; color: var(--leaf-green); margin-top: 2px;
  }
  .address {
    font-size: 22px; line-height: 1.3; margin-top: 28px;
  }
  .contact-list {
    list-style: none; margin-top: 28px;
    font-size: 22px; line-height: 1.35;
  }
  .contact-list li { display: flex; align-items: center; gap: 12px; white-space: nowrap; }
  .contact-list svg { width: 20px; height: 20px; flex: none; }

  .services-bar {
    position: absolute; left: 96px; right: 96px; top: 470px;
    height: 34px; border-radius: 17px;
    background: var(--leaf-green);
    display: flex; align-items: center; justify-content: center; gap: 22px;
    color: #fff; font-size: 18px; font-weight: 600; font-style: italic;
  }
  .services-bar span::before {
    content: "\2022"; margin-right: 8px; font-style: normal;
  }
</style>
</head>
<body>
  <div class="card">
    <div class="side-band left"></div>
    <div class="side-band right"></div>
    <div class="edge-rule left"></div>
    <div class="edge-rule right"></div>

    <div class="brand">
      <span class="brand-dot"></span>
      <span class="brand-name">Belmora Yards</span>
    </div>

    <div class="column-divider"></div>

    <div class="contact">
      <div class="person-name">Trevor Hollis</div>
      <div class="person-title">WPMB Certified Applicator</div>
      <div class="address">48260 Pinecrest<br>Westbrook, KS 66019</div>
      <ul class="contact-list">
        <li>
          <svg viewBox="0 0 20 20" aria-hidden="true"><rect x="5" y="1" width="10" height="18" rx="2" fill="none" stroke="#5fa42a" stroke-width="2"/><circle cx="10" cy="15.5" r="1.2" fill="#5fa42a"/></svg>
          (913) 555-0148
        </li>
        <li>
          <svg viewBox="0 0 20 20" aria-hidden="true"><circle cx="10" cy="10" r="3.5" fill="none" stroke="#5fa42a" stroke-width="2"/><path d="M13.5 10v1.5a2.5 2.5 0 0 0 5 0V10a8.5 8.5 0 1 0-3.4 6.8" fill="none" stroke="#5fa42a" stroke-width="2"/></svg>
          trevor@belmorayards.com
        </li>
        <li>
          <svg viewBox="0 0 20 20" aria-hidden="true"><circle cx="10" cy="10" r="8.5" fill="none" stroke="#5fa42a" stroke-width="1.8"/><ellipse cx="10" cy="10" rx="3.8" ry="8.5" fill="none" stroke="#5fa42a" stroke-width="1.5"/><path d="M1.5 10h17M3 5.5h14M3 14.5h14" stroke="#5fa42a" stroke-width="1.5"/></svg>
          belmorayards.com
        </li>
      </ul>
    </div>

    <div class="services-bar">
      <span>Fertilization</span>
      <span>Weed Control</span>
      <span>Aeration</span>
      <span>Verticutting</span>
      <span>Seeding</span>
    </div>
  </div>
</body>
</html>
```